Stress Fracture Infographic for Scientific Paper

We need an infographic for a research/scientific paper. We would like the infographic to give readers a clear and eye-catching overview about the factors that put athletes and military personnel at risk for stress fractures. The design needs to communicate that the risk factors are cumulative and interactive; however, how they specifically accumulate and interact has not been studied or shown in the literature (we need healthcare providers who subjectively assess cumulative risk profiles in athletes and we concurrently need scientists to evaluate the interdependence of risk factors). We define cumulative risk profile as: a subjective clinical determination of the number of factors putting an athlete at risk along with thoughtful consideration regarding how all the risk factors interact with one another. We would like the infographic to display this cumulative risk profile idea.

The risk factors can be categorized as:
INTRINSIC-
Non-modifiable (such as sex, race, age, genetics, anatomical structure, and prior bone stress injury), modifiable (muscle strength, muscle fatigue, flexibility, biomechanics, stress, recovery strategies, nutrition, energy deficiency), unclear if modifiable, not, or somewhere in between (such as gut health);

EXTRINSIC-
Modifiable (footwear, training surface, workload)

Target Market(s)

Researchers and clinicians

Requirements
Must have
• A scientific feel
Nice to have
• Creative way to display the cumulative and interactive impact of risk factors
Should not have
• Too cartoon-ish or child-like feel

```html
<!DOCTYPE html>
<html lang="en">
<head>
<meta charset="utf-8">
<title>The Risk Factors</title>
<link href="https://fonts.googleapis.com/css2?family=Bebas+Neue&family=Poppins:wght@400;500&display=swap" rel="stylesheet">
<style>
  :root {
    --banner: #0f9cba;
    --banner-dark: #1c6d7f;
    --banner-shade: #1a5465;
    --teal-deep: #1c6478;
    --ink: #1d2f36;
    --sky: #c4e2eb;
    --sky-light: #d3eaf1;
    --paper: #f7fbfc;
    --white: #ffffff;
  }
  * { margin: 0; padding: 0; box-sizing: border-box; }
  html, body { width: 862px; height: 1200px; overflow: hidden; background: var(--paper); }
  .poster {
    position: relative; width: 862px; height: 1200px; overflow: hidden;
    background: var(--paper);
    font-family: "Poppins", sans-serif; color: var(--ink);
  }
  .header-art { position: absolute; left: 0; top: 0; width: 862px; height: 260px; }
  .title {
    position: absolute; left: 134px; top: 58px; width: 592px; text-align: center;
    font-family: "Bebas Neue", sans-serif; font-size: 86px; line-height: 86px;
    color: var(--white); letter-spacing: 1px;
    text-shadow: 3px 3px 0 var(--banner-shade);
  }
  .intro {
    position: absolute; left: 110px; top: 172px; width: 642px; text-align: center;
    font-size: 15.5px; line-height: 19px; font-weight: 500; color: var(--ink);
  }
  .field {
    position: absolute; left: 0; top: 262px; width: 862px; height: 925px;
    background: var(--sky);
  }
  .column {
    position: absolute; top: 585px; height: 590px; background: var(--sky-light); opacity: .7;
  }
  .tree { position: absolute; left: 0; top: 0; width: 862px; height: 600px; }
  .group-label {
    font-family: "Bebas Neue", sans-serif; fill: var(--teal-deep); font-size: 48px;
  }
  .badge-label {
    font-family: "Bebas Neue", sans-serif; fill: var(--ink); font-size: 19px;
  }
  .such-as {
    position: absolute; top: 560px; width: 110px; text-align: center;
    font-size: 15px; font-weight: 500; color: var(--ink);
    border-bottom: 3px solid var(--teal-deep); padding-bottom: 1px;
  }
  .factor-list { position: absolute; top: 592px; width: 160px; list-style: none; }
  .factor { position: absolute; left: 0; width: 160px; text-align: center; }
  .factor-icon {
    display: block; margin: 0 auto; width: 38px; height: 38px; border-radius: 50%;
    background: var(--teal-deep); border: 3px solid var(--banner);
    box-shadow: inset 0 0 0 2px var(--white);
  }
  .factor-name {
    display: block; margin-top: 4px; font-size: 15.5px; line-height: 15px; color: var(--ink);
  }
  .device-scene {
    position: absolute; left: 433px; top: 885px; width: 375px; height: 300px;
    background: linear-gradient(160deg, #3f8fc7 0%, #2b6fa6 45%, #e3b996 100%);
    border-radius: 14px 14px 0 0;
  }
  .footer-band {
    position: absolute; left: 0; bottom: 0; width: 862px; height: 13px; background: var(--banner);
  }
  .footer-rule {
    position: absolute; left: 0; bottom: 16px; width: 862px; height: 3px; background: var(--banner);
  }
</style>
</head>
<body>
<main class="poster">

  <svg class="header-art" viewBox="0 0 862 260" aria-hidden="true">
    <!-- hairlines above and below the ribbon -->
    <line x1="215" y1="45" x2="406" y2="45" stroke="var(--banner)" stroke-width="2"/>
    <line x1="410" y1="45" x2="417" y2="45" stroke="var(--banner)" stroke-width="2"/>
    <line x1="585" y1="45" x2="698" y2="45" stroke="var(--banner)" stroke-width="2"/>
    <line x1="263" y1="155" x2="325" y2="155" stroke="var(--banner)" stroke-width="2"/>
    <line x1="456" y1="155" x2="462" y2="155" stroke="var(--banner)" stroke-width="2"/>
    <line x1="474" y1="155" x2="665" y2="155" stroke="var(--banner)" stroke-width="2"/>
    <!-- ribbon tails -->
    <polygon points="55,88 134,88 134,182 55,182 80,135" fill="var(--banner-dark)"/>
    <polygon points="807,88 728,88 728,182 807,182 782,135" fill="var(--banner-dark)"/>
    <polygon points="134,148 172,148 172,182" fill="var(--banner-shade)"/>
    <polygon points="726,148 689,148 689,182" fill="var(--banner-shade)"/>
    <!-- ribbon face -->
    <rect x="134" y="54" width="592" height="94" fill="var(--banner)" stroke="var(--white)" stroke-width="2"/>
  </svg>

  <h1 class="title">The Risk Factors</h1>
  <p class="intro">A subjective clinical determination of the number of factors putting an athlete at risk along with thoughtful consideration regarding how all the risk factors interact with one another.</p>

  <section class="field">
    <div class="column" style="left:42px;width:136px;top:322px;"></div>
    <div class="column" style="left:201px;width:156px;top:322px;"></div>
    <div class="column" style="left:370px;width:136px;top:322px;"></div>
    <div class="column" style="left:632px;width:136px;top:322px;"></div>
  </section>

  <svg class="tree" viewBox="0 0 862 600" aria-hidden="true">
    <g fill="none" stroke="var(--teal-deep)" stroke-width="1.6">
      <polyline points="194,399 194,425 109,425 109,450"/>
      <line x1="273" y1="399" x2="273" y2="450"/>
      <polyline points="352,399 352,425 437,425 437,450"/>
      <line x1="699" y1="399" x2="699" y2="450"/>
    </g>
    <g fill="var(--teal-deep)">
      <circle cx="194" cy="399" r="7"/><circle cx="273" cy="399" r="7"/>
      <circle cx="352" cy="399" r="7"/><circle cx="699" cy="399" r="7"/>
    </g>

    <!-- group pills -->
    <g>
      <rect x="170" y="296" width="208" height="90" rx="45" fill="var(--white)" stroke="var(--teal-deep)" stroke-width="8"/>
      <rect x="186" y="312" width="176" height="58" rx="29" fill="none" stroke="var(--banner)" stroke-width="2"/>
      <circle cx="166" cy="341" r="6" fill="var(--white)" stroke="var(--teal-deep)" stroke-width="2"/>
      <circle cx="382" cy="341" r="6" fill="var(--white)" stroke="var(--teal-deep)" stroke-width="2"/>
      <text class="group-label" x="274" y="359" text-anchor="middle">INTRINSIC</text>
    </g>
    <g>
      <rect x="595" y="296" width="208" height="90" rx="45" fill="var(--white)" stroke="var(--teal-deep)" stroke-width="8"/>
      <rect x="611" y="312" width="176" height="58" rx="29" fill="none" stroke="var(--banner)" stroke-width="2"/>
      <circle cx="591" cy="341" r="6" fill="var(--white)" stroke="var(--teal-deep)" stroke-width="2"/>
      <circle cx="807" cy="341" r="6" fill="var(--white)" stroke="var(--teal-deep)" stroke-width="2"/>
      <text class="group-label" x="699" y="359" text-anchor="middle">EXTRINSIC</text>
    </g>

    <!-- category badges -->
    <g id="badge-a">
      <circle cx="109" cy="505" r="55" fill="var(--teal-deep)"/>
      <circle cx="109" cy="505" r="50" fill="none" stroke="var(--white)" stroke-width="2" stroke-dasharray="5 3"/>
      <circle cx="109" cy="505" r="43" fill="var(--white)"/>
      <text class="badge-label" x="109" y="501" text-anchor="middle">NON-</text>
      <text class="badge-label" x="109" y="521" text-anchor="middle">MODIFIABLE</text>
    </g>
    <g>
      <circle cx="273" cy="505" r="55" fill="var(--teal-deep)"/>
      <circle cx="273" cy="505" r="50" fill="none" stroke="var(--white)" stroke-width="2" stroke-dasharray="5 3"/>
      <circle cx="273" cy="505" r="43" fill="var(--white)"/>
      <text class="badge-label" x="273" y="512" text-anchor="middle">MODIFIABLE</text>
    </g>
    <g>
      <circle cx="437" cy="505" r="55" fill="var(--teal-deep)"/>
      <circle cx="437" cy="505" r="50" fill="none" stroke="var(--white)" stroke-width="2" stroke-dasharray="5 3"/>
      <circle cx="437" cy="505" r="43" fill="var(--white)"/>
      <text class="badge-label" x="437" y="492" text-anchor="middle">SOMEWHERE</text>
      <text class="badge-label" x="437" y="511" text-anchor="middle">IN</text>
      <text class="badge-label" x="437" y="530" text-anchor="middle">BETWEEN</text>
    </g>
    <g>
      <circle cx="699" cy="505" r="55" fill="var(--teal-deep)"/>
      <circle cx="699" cy="505" r="50" fill="none" stroke="var(--white)" stroke-width="2" stroke-dasharray="5 3"/>
      <circle cx="699" cy="505" r="43" fill="var(--white)"/>
      <text class="badge-label" x="699" y="512" text-anchor="middle">MODIFIABLE</text>
    </g>
  </svg>

  <div class="such-as" style="left:54px;">- SUCH AS -</div>
  <div class="such-as" style="left:218px;">- SUCH AS -</div>
  <div class="such-as" style="left:382px;">- SUCH AS -</div>
  <div class="such-as" style="left:644px;">- SUCH AS -</div>

  <ul class="factor-list" style="left:29px;">
    <li class="factor" style="top:0;"><span class="factor-icon"></span><span class="factor-name">Sex</span></li>
    <li class="factor" style="top:69px;"><span class="factor-icon"></span><span class="factor-name">Race</span></li>
    <li class="factor" style="top:139px;"><span class="factor-icon"></span><span class="factor-name">Age</span></li>
    <li class="factor" style="top:212px;"><span class="factor-icon"></span><span class="factor-name">Genetics</span></li>
    <li class="factor" style="top:280px;"><span class="factor-icon"></span><span class="factor-name">Anatomical<br>structure</span></li>
    <li class="factor" style="top:363px;"><span class="factor-icon"></span><span class="factor-name">Prior bone<br>stress injury</span></li>
  </ul>

  <ul class="factor-list" style="left:193px;">
    <li class="factor" style="top:0;"><span class="factor-icon"></span><span class="factor-name">Muscle strength</span></li>
    <li class="factor" style="top:69px;"><span class="factor-icon"></span><span class="factor-name">Muscle fatigue</span></li>
    <li class="factor" style="top:139px;"><span class="factor-icon"></span><span class="factor-name">Flexibility</span></li>
    <li class="factor" style="top:212px;"><span class="factor-icon"></span><span class="factor-name">Biomechanics</span></li>
    <li class="factor" style="top:280px;"><span class="factor-icon"></span><span class="factor-name">Stress</span></li>
    <li class="factor" style="top:351px;"><span class="factor-icon"></span><span class="factor-name">Recovery<br>strategies</span></li>
    <li class="factor" style="top:434px;"><span class="factor-icon"></span><span class="factor-name">Nutrition</span></li>
    <li class="factor" style="top:503px;"><span class="factor-icon"></span><span class="factor-name">Energy deficiency</span></li>
  </ul>

  <ul class="factor-list" style="left:357px;">
    <li class="factor" style="top:0;"><span class="factor-icon"></span><span class="factor-name">Gut health</span></li>
  </ul>

  <ul class="factor-list" style="left:619px;">
    <li class="factor" style="top:0;"><span class="factor-icon"></span><span class="factor-name">Footwear</span></li>
    <li class="factor" style="top:69px;"><span class="factor-icon"></span><span class="factor-name">Training surface</span></li>
    <li class="factor" style="top:139px;"><span class="factor-icon"></span><span class="factor-name">Workload</span></li>
  </ul>

  <div class="device-scene" role="img" aria-label="Illustration of two hands holding a tablet showing a body diagram and health readings"></div>

  <div class="footer-rule"></div>
  <div class="footer-band"></div>
</main>
</body>
</html>
```